Design for a 4 screens iOS and Android app - "TrajiMesur"

The app allows you to track your car gasoline refill ...
We need a design for the 4 screens of the app:
a) 1 form with 3 fields.
b) 1 simple list view
c) 1 summary view
d) 1 text page
2 "alerts" items are also to be designed.
No specific guidelines, nor logo or whatever.
It will be a free app distributed on iOS and Androïd.
We just want to make it looking nice & very usable for end users.
Target Market(s)
B2C app
Industry/Entity Type
Android

```html
<!DOCTYPE html>
<html lang="fr">
<head>
<meta charset="utf-8">
<title>TrajiMesur – Statistics</title>
<link rel="stylesheet" href="https://fonts.googleapis.com/css2?family=Roboto:wght@400;500&display=swap">
<style>
:root{
  --status-bar:#10354a;
  --app-bar:#1c6688;
  --on-primary:#ffffff;
  --tab-muted:#dfeaf0;
  --surface:#ffffff;
  --divider:#d9d9d9;
  --text-strong:#141414;
  --text-muted:#777777;
  --nav-bar:#000000;
}
*{box-sizing:border-box;margin:0;padding:0}
html,body{width:675px;height:1200px;overflow:hidden;background:var(--surface)}
body{font-family:"Roboto",Arial,sans-serif;position:relative}
.status-bar{position:absolute;top:0;left:0;width:675px;height:45px;background:var(--status-bar);color:var(--on-primary);display:flex;align-items:center;justify-content:flex-end;gap:14px;padding-right:19px}
.status-bar .clock{font-size:22px;margin-left:4px}
.app-bar{position:absolute;top:45px;left:0;width:675px;height:171px;background:var(--app-bar);color:var(--on-primary);box-shadow:0 2px 4px rgba(0,0,0,.25);z-index:2}
.app-bar .back{position:absolute;left:32px;top:30px}
.app-bar .title{position:absolute;left:138px;top:20px;font-size:36px;font-weight:400;line-height:48px}
.tabs{position:absolute;left:0;bottom:0;width:100%;height:79px;display:flex}
.tab{flex:1;display:flex;align-items:center;justify-content:center;font-size:20.5px;letter-spacing:.3px;text-transform:uppercase;color:var(--tab-muted);position:relative;padding-bottom:6px}
.tab.active{color:var(--on-primary)}
.tab.active::after{content:"";position:absolute;left:0;right:0;bottom:0;height:4px;background:var(--on-primary)}
.refill-list{position:absolute;top:216px;left:0;width:675px;list-style:none}
.refill-date,.refill-details{display:flex;align-items:center;border-bottom:1px solid var(--divider)}
.refill-date{height:103px;padding:0 28px 0 45px;justify-content:space-between;font-size:26.5px;color:var(--text-strong)}
.refill-list li:first-child .refill-date{height:113px}
.refill-details{height:103px;padding:0 39px 0 36px;font-size:24.5px;color:var(--text-muted)}
.refill-details .distance{width:290px}
.refill-details .volume{flex:1}
.refill-list li:last-child .refill-details{border-bottom:none}
.nav-bar{position:absolute;left:0;bottom:0;width:675px;height:86px;background:var(--nav-bar);display:flex;align-items:center;justify-content:space-around;padding:0 95px}
</style>
</head>
<body>
<header class="status-bar">
  <svg width="20" height="26" viewBox="0 0 20 26" aria-hidden="true"><path d="M10 1a8 8 0 0 0-8 8c0 6 8 16 8 16s8-10 8-16a8 8 0 0 0-8-8zm0 11a3 3 0 1 1 0-6 3 3 0 0 1 0 6z" fill="#fff"/></svg>
  <svg width="32" height="24" viewBox="0 0 32 24" aria-hidden="true"><path d="M16 23L0 5a24 24 0 0 1 32 0z" fill="#fff"/></svg>
  <svg width="26" height="26" viewBox="0 0 26 26" aria-hidden="true"><path d="M1 25L25 1v24z" fill="#fff"/></svg>
  <svg width="16" height="27" viewBox="0 0 16 27" aria-hidden="true"><rect x="5" y="0" width="6" height="3" fill="#fff"/><rect x="0" y="3" width="16" height="24" fill="#fff"/></svg>
  <span class="clock">10:55</span>
</header>

<section class="app-bar">
  <svg class="back" width="32" height="28" viewBox="0 0 32 28" aria-label="Back"><path d="M30 14H4M15 2L3 14l12 12" fill="none" stroke="#fff" stroke-width="4"/></svg>
  <h1 class="title">Statistics</h1>
  <nav class="tabs">
    <div class="tab">Summary</div>
    <div class="tab active">List</div>
  </nav>
</section>

<ul class="refill-list">
  <li><div class="refill-date"><span>15 février 2016</span><span>14:24</span></div>
      <div class="refill-details"><span class="distance">7500 km</span><span class="volume">6.5 l</span><span>570.54 €</span></div></li>
  <li><div class="refill-date"><span>15 février 2016</span><span>14:24</span></div>
      <div class="refill-details"><span class="distance">7500 km</span><span class="volume">6.5 l</span><span>570.54 €</span></div></li>
  <li><div class="refill-date"><span>15 février 2016</span><span>14:24</span></div>
      <div class="refill-details"><span class="distance">7500 km</span><span class="volume">6.5 l</span><span>570.54 €</span></div></li>
  <li><div class="refill-date"><span>15 février 2016</span><span>14:24</span></div>
      <div class="refill-details"><span class="distance">7500 km</span><span class="volume">6.5 l</span><span>570.54 €</span></div></li>
</ul>

<footer class="nav-bar">
  <svg width="30" height="32" viewBox="0 0 30 32" aria-label="Back"><path d="M27 3v26L3 16z" fill="none" stroke="#fff" stroke-width="3" stroke-linejoin="round"/></svg>
  <svg width="32" height="32" viewBox="0 0 32 32" aria-label="Home"><circle cx="16" cy="16" r="13.5" fill="none" stroke="#fff" stroke-width="3"/></svg>
  <svg width="30" height="30" viewBox="0 0 30 30" aria-label="Recent apps"><rect x="2" y="2" width="26" height="26" rx="2" fill="none" stroke="#fff" stroke-width="3"/></svg>
</footer>
</body>
</html>
```